Online bill payment portal website design

Online Invoice Payment Website

The customer will click on the logos of the institution they want to pay and the payment will be made at the latest stage to write the customer number.

Invoice payment can be made online. Telephone, Television, Internet, Electricity, Water, Natural Gas, and all institutional payments.

Example website : https://www.zenitodeme.com/

Industry/Entity Type

Invoice

Logo Text

HizliBorcKapat.Net

Number of Pages Required

4 page

Font styles to use
Serif
Sans Serif

Colors
abd036
33a6d7
876aae
e667a6
ec1f27
f37122
85abd2
0555a3
00a990

Requirements
Must have
• Logos of payment institutions
• Credit Card Payment form
• Customer information form
• COntact page
• List of Institutions
• Accept privacy policies in all forms
Nice to have
• Good and new design :)
Should not have
• Same with zenitodeme.com ! i want new site

```html
<!DOCTYPE html>
<html lang="en">
<head>
<meta charset="utf-8">
<title>Tahsilo – Online Invoice Payment</title>
<link href="https://fonts.googleapis.com/css2?family=Montserrat:wght@300;400;500;600;700;800&display=swap" rel="stylesheet">
<style>
:root{
  --brand:#0555a3;
  --text:#333a44;
  --line:#dcdfe3;
  --band:#f4f4f4;
  --green:#abd036;
  --purple:#876aae;
  --pink:#e667a6;
  --red:#ec1f27;
  --orange:#f37122;
  --teal:#00a990;
  --company:#3e4a5c;
}
*{box-sizing:border-box;margin:0;padding:0}
html,body{width:987px;height:1200px;overflow:hidden;background:#fff}
body{position:relative;font-family:'Montserrat',sans-serif;color:var(--text)}
.site-header{position:absolute;top:0;left:0;width:987px;height:72px}
.brand{position:absolute;left:116px;top:24px;font-size:22px;font-weight:700;color:var(--brand);letter-spacing:.2px}
.main-nav{position:absolute;top:32px;left:422px;display:flex;font-size:12px;color:#3a3f46}
.main-nav a{text-decoration:none;color:inherit;margin-right:36px}
.main-nav a.active{color:var(--brand)}
.search-btn{position:absolute;left:833px;top:25px;width:28px;height:28px;border-radius:50%;background:var(--brand)}
.search-btn svg{position:absolute;left:8px;top:8px}
.hero{position:absolute;top:72px;left:0;width:987px;height:502px;background:linear-gradient(120deg,#5a8cc8,#4578b9 55%,#3d70b2)}
.hero-title{position:absolute;top:244px;left:0;width:987px;text-align:center;color:#fff;font-weight:400;font-size:29px;letter-spacing:.3px}
.hero-btn{position:absolute;left:415px;top:312px;width:157px;height:44px;border:1px solid #fff;border-radius:3px;color:#fff;font-size:12px;text-align:center;line-height:42px;letter-spacing:.5px}
.hero-arrow{position:absolute;top:246px}
.companies-title{position:absolute;top:622px;left:0;width:987px;text-align:center;font-size:19px;font-weight:400;color:#3e434a;letter-spacing:.4px}
.company-grid{position:absolute;top:688px;left:117px;display:grid;grid-template-columns:repeat(4,174px);column-gap:18px;row-gap:18px}
.company{height:95px;border:1px solid var(--line);display:flex;align-items:center;justify-content:center;font-size:22px;font-weight:600;color:var(--company)}
.dots{position:absolute;top:928px;left:459px;display:flex;gap:12px}
.dots span{width:8px;height:8px;border-radius:50%;background:#e3e5e8}
.dots span.on{background:var(--brand)}
.categories{position:absolute;top:955px;left:0;width:987px;height:190px;background:var(--band)}
.tile{position:absolute;top:46px;width:109px;height:96px;color:#fff;font-size:9px;font-weight:700;text-align:center}
.tile svg{position:absolute;left:44px;top:36px}
.tile span{position:absolute;left:0;width:100%;top:72px}
.site-footer{position:absolute;top:1145px;left:0;width:987px;height:55px}
.footer-brand{position:absolute;left:120px;top:20px;font-size:17px;font-weight:700;color:#222}
.pay-options{position:absolute;left:276px;top:20px;display:flex;align-items:center;font-size:8px;font-weight:500;color:#222}
.pay-options b{font-weight:500;margin-right:5px}
.card{width:29px;height:18px;border:1px solid var(--line);margin-right:5px;font-size:6px;text-align:center;line-height:16px;color:#666}
.copyright{position:absolute;left:660px;top:22px;font-size:9px;color:#222}
</style>
</head>
<body>
<header class="site-header">
  <div class="brand">Tahsilo</div>
  <nav class="main-nav">
    <a class="active" href="#">Home</a><a href="#">About Us</a><a href="#">Features</a><a href="#">Pricing</a><a href="#">Contact Us</a>
  </nav>
  <div class="search-btn"><svg width="12" height="12" viewBox="0 0 12 12"><circle cx="5" cy="5" r="3.5" fill="none" stroke="#fff" stroke-width="1.8"/><line x1="7.6" y1="7.6" x2="10.5" y2="10.5" stroke="#fff" stroke-width="1.8" stroke-linecap="round"/></svg></div>
</header>

<section class="hero" role="img" aria-label="Smiling man on the phone holding a bank card at his laptop, tinted blue">
  <svg class="hero-arrow" style="left:56px" width="20" height="30" viewBox="0 0 20 30"><path d="M15 3 L4 15 L15 27" fill="none" stroke="#fff" stroke-width="3.5"/></svg>
  <h1 class="hero-title">We are an Online Invoice Payment Website</h1>
  <div class="hero-btn">LEARN MORE</div>
  <svg class="hero-arrow" style="left:912px" width="20" height="30" viewBox="0 0 20 30"><path d="M5 3 L16 15 L5 27" fill="none" stroke="#fff" stroke-width="3.5"/></svg>
</section>

<h2 class="companies-title">SELECT YOUR ONLINE INVOICE PAYMENT COMPANY</h2>
<div class="company-grid">
  <div class="company">Zelvora</div>
  <div class="company">Brimtal</div>
  <div class="company">Quorvex</div>
  <div class="company">Talvenn</div>
  <div class="company">Ordisca</div>
  <div class="company">Merovin</div>
  <div class="company">Pexarel</div>
  <div class="company">Corvessa</div>
</div>
<div class="dots"><span class="on"></span><span></span><span></span><span></span></div>

<section class="categories">
  <div class="tile" style="left:119px;background:var(--green)"><svg width="20" height="20" viewBox="0 0 20 20"><path d="M5 3c1-1 2 0 3 2s0 2-1 3c1 2 2 3 4 4 1-1 1-2 3-1s3 2 2 3-2 2-4 1C8 13 6 10 4 6 3 4 4 4 5 3z" fill="#fff"/></svg><span>TELEPHONE</span></div>
  <div class="tile" style="left:250px;background:var(--purple)"><svg width="20" height="20" viewBox="0 0 20 20"><rect x="2" y="6" width="16" height="11" rx="2" fill="none" stroke="#fff" stroke-width="2"/><path d="M7 2l3 4 3-4" fill="none" stroke="#fff" stroke-width="1.6"/></svg><span>TELEVISION</span></div>
  <div class="tile" style="left:376px;background:var(--pink)"><svg width="20" height="20" viewBox="0 0 20 20" fill="none" stroke="#fff" stroke-width="1.5"><circle cx="10" cy="10" r="8"/><ellipse cx="10" cy="10" rx="3.5" ry="8"/><line x1="2" y1="10" x2="18" y2="10"/><line x1="3.5" y1="6" x2="16.5" y2="6"/><line x1="3.5" y1="14" x2="16.5" y2="14"/></svg><span>INTERNET</span></div>
  <div class="tile" style="left:504px;background:var(--red)"><svg width="20" height="20" viewBox="0 0 20 20" fill="#fff"><rect x="4" y="2" width="2" height="8"/><rect x="8" y="4" width="2" height="6"/><rect x="2" y="10" width="16" height="8"/></svg><span>ELECTRICITY</span></div>
  <div class="tile" style="left:633px;background:var(--orange)"><svg width="20" height="20" viewBox="0 0 20 20"><path d="M10 2C7 7 5 9 5 12a5 5 0 0 0 10 0c0-3-2-5-5-10z" fill="#fff"/></svg><span>WATER</span></div>
  <div class="tile" style="left:762px;background:var(--teal)"><svg width="20" height="20" viewBox="0 0 20 20" fill="#fff"><rect x="7" y="7" width="6" height="12" rx="2"/><rect x="8.5" y="3" width="3" height="4"/><path d="M11 4h5v1.5h-5z"/></svg><span>NATURAL GAS</span></div>
</section>

<footer class="site-footer">
  <div class="footer-brand">Tahsilo</div>
  <div class="pay-options"><b>PAYMENT OPTIONS</b>
    <div class="card">Cardo</div><div class="card">Orbi</div><div class="card">Mira</div><div class="card">Payly</div><div class="card">Novo</div>
  </div>
  <div class="copyright">© 2017 Company Name &nbsp;|&nbsp;&nbsp; All Rights Reserved</div>
</footer>
</body>
</html>
```